Business Card,

Keystone Ridge & Holdings LLC (DBA Tallow Dwellings) is a licensed residential contractor in Southwest Louisiana, specializing in custom homes, remodels, additions, and Sheltered Crest roof systems.

We’re looking for a designer who can capture the look and feel of a modern, trustworthy Southern-style builder — a brand that communicates craftsmanship, class, and confidence at a glance.

This design package will be used for client meetings, door-to-door marketing, and online advertising, so we need visuals that stand out both in-hand and on screen.

Target Market(s)

Ages 30–65 Married or family-oriented Household income $85,000+ Own or are purchasing a home and want upgrades, additions, or complete rebuilds Value craftsmanship, reliability, and financing flexibility ($0 down options) Respond well to clear before/after visuals, trust-based branding, and professional presentation 🧠 Design cue: They’re not looking for the cheapest contractor — they want someone they can trust with their home and their money. Designs should look professional, clean, and confident.

Industry/Entity Type

Residential Construction, Custom Home Building & Remodeling

Contact Information for Business Card

Logo, "Tallow Dwellings", “Proudly serving Southwest Louisiana with Quality Craftsmanship & Financing Options”, Full Name + Title Everett Pruitt Licensed Residential Contractor | LA #413962, Financing Options QR Code, Phone :337-529-7830 Email: Everett@tallowdwellings.net, Website: www.keystoneridgebuilders.homes , Service Area: Lake Charles & Surrounding Areas ,“Fully Licensed & Insured” ,A small 5-star icon with “Rated 5 Stars by Local Homeowners” , “Schedule Your Free Design-Build Starter Session Today!”

Font styles to use
Other font styles liked:
• Montserrat Bold for business name, Lora Italic for tagline, open sans regular for contact info,

Colors
0054AA
0677BA
7BADD7
CADEEF
E8F1F8

Requirements
Must have
• (Deep Navy (#1 Color) and Gold or rich metallic accent color) “$0 Down Financing Available” and the QR Code Name, Title, and direct Contact Info, Custom Homes • Additions • Remodels • Sheltered Roofing
Nice to have
• 5 Star Searchly Icon, “Refer a friend — Earn $500 when they build with us.”, Facebook.com/keystoneridgebld
Should not have
• Don’t Cram 10 services, slogans, or contact details. Don’t Mix random colors or fonts to “stand out.”, Don’t Use hammer or roof clip art., Don’t Use script, gothic, or cursive fonts., Don’t Add loud textures or frames.

```html
<!DOCTYPE html>
<html lang="en">
<head>
<meta charset="utf-8">
<title>Tallow Dwellings – Business Card</title>
<link href="https://fonts.googleapis.com/css2?family=Montserrat:wght@800&family=Catamaran:wght@400;500&family=Josefin+Sans:wght@400;600&display=swap" rel="stylesheet">
<style>
  :root{
    --stage:#5b5b5d;
    --card:#050606;
    --gold:#e7c862;
    --gold-text:#f0d978;
    --ink:#0b0b0b;
    --faint:#2e2b24;
    --band:linear-gradient(90deg,#a8792c 0%,#d8b555 22%,#c89a3e 40%,#f5e48a 62%,#c28f38 80%,#e0c160 100%);
    --band-back:linear-gradient(90deg,#b0842f 0%,#e6cf6e 22%,#a8702a 45%,#d9bb58 60%,#f6e688 76%,#b3842f 100%);
  }
  *{margin:0;padding:0;box-sizing:border-box}
  html,body{width:1200px;height:960px;overflow:hidden;background:var(--stage)}
  .card{position:absolute;width:774px;height:442px;background:var(--card);overflow:hidden}
  .card--front{left:74px;top:37px}
  .card--back{left:321px;top:499px}
  .band{position:absolute;left:0;width:100%;background:var(--band)}
  .card--back .band{background:var(--band-back)}
  .band--name{top:66px;height:48px}
  .band--cta,.band--footer{height:27px;display:flex;align-items:center;justify-content:center;
    font-family:"Catamaran",sans-serif;font-weight:500;color:var(--ink);font-size:19px}
  .band--cta{top:391px}
  .band--top{top:28px;height:27px}
  .band--footer{top:386px;font-size:18.5px}
  .holder-name{position:absolute;left:42px;top:68px;font-family:"Montserrat",sans-serif;font-weight:800;
    font-size:34px;line-height:44px;color:var(--ink);letter-spacing:-.3px}
  .holder-title{position:absolute;left:42px;top:122px;font-family:"Catamaran",sans-serif;font-size:19px;color:var(--gold-text)}
  .watermark{position:absolute;left:244px;top:118px;width:284px;height:228px;border:3px solid var(--faint)}
  .contacts{position:absolute;left:42px;top:270px;list-style:none;font-family:"Catamaran",sans-serif;
    font-size:19px;color:var(--gold-text)}
  .contacts li{display:flex;align-items:center;height:25px;margin-bottom:0}
  .contacts li:first-child{margin-bottom:7px}
  .contacts svg{width:20px;height:20px;margin-right:16px;fill:var(--gold-text)}
  .trust{position:absolute;right:34px;top:288px;text-align:right;font-family:"Catamaran",sans-serif;
    font-size:19px;color:var(--gold-text);line-height:1}
  .stars{display:block;margin:8px 0 8px auto;width:176px;height:32px}
  .brand-mark{position:absolute;left:307px;top:102px;width:158px;height:139px;border:2.5px solid var(--gold)}
  .brand-name{position:absolute;left:0;width:100%;top:253px;text-align:center;font-family:"Josefin Sans",sans-serif;
    font-weight:400;font-size:46px;color:var(--gold);letter-spacing:1px}
  .brand-tagline{position:absolute;left:0;width:100%;top:314px;text-align:center;font-family:"Josefin Sans",sans-serif;
    font-weight:600;font-size:22px;letter-spacing:6px;color:var(--gold-text)}
</style>
</head>
<body>
<svg width="0" height="0" style="position:absolute" aria-hidden="true">
  <defs>
    <linearGradient id="starGold" x1="0" y1="0" x2="0" y2="1">
      <stop offset="0" stop-color="#f6e08a"/><stop offset="1" stop-color="#c8962f"/>
    </linearGradient>
    <polygon id="star" points="16,1 20,11.5 31,12 22.5,19 25.5,30 16,23.8 6.5,30 9.5,19 1,12 12,11.5"/>
  </defs>
</svg>

<section class="card card--front">
  <div class="band band--name"></div>
  <h1 class="holder-name">EVERETT PRUITT</h1>
  <p class="holder-title">Licensed Residential Contractor</p>
  <div class="watermark" role="img" aria-label="Faint Tallow Dwellings brand mark"></div>
  <ul class="contacts">
    <li><svg viewBox="0 0 24 24"><path d="M12 1a8 8 0 0 0-8 8c0 6 8 14 8 14s8-8 8-14a8 8 0 0 0-8-8zm0 11a3 3 0 1 1 0-6 3 3 0 0 1 0 6z"/></svg>LA #413962, Financing</li>
    <li><svg viewBox="0 0 24 24"><path d="M6.6 10.8a15 15 0 0 0 6.6 6.6l2.2-2.2a1 1 0 0 1 1-.25 11.4 11.4 0 0 0 3.6.6 1 1 0 0 1 1 1V20a1 1 0 0 1-1 1A17 17 0 0 1 3 4a1 1 0 0 1 1-1h3.5a1 1 0 0 1 1 1c0 1.25.2 2.45.6 3.6a1 1 0 0 1-.25 1z"/></svg>337-529-7830</li>
    <li><svg viewBox="0 0 24 24"><path d="M2 9l10-6 10 6v12H2zm2 1.5V19h16v-8.5l-8 5z"/></svg>Everett@tallowdwellings.net</li>
    <li><svg viewBox="0 0 24 24"><path d="M12 2a10 10 0 1 0 0 20 10 10 0 0 0 0-20zm6.9 9h-3a15 15 0 0 0-1.3-6A8 8 0 0 1 18.9 11zM12 4.1c.9 1.3 1.7 3.6 1.9 6.9h-3.8c.2-3.3 1-5.6 1.9-6.9zM9.4 5a15 15 0 0 0-1.3 6h-3A8 8 0 0 1 9.4 5zM5.1 13h3a15 15 0 0 0 1.3 6A8 8 0 0 1 5.1 13zm6.9 6.9c-.9-1.3-1.7-3.6-1.9-6.9h3.8c-.2 3.3-1 5.6-1.9 6.9zm2.6-.9a15 15 0 0 0 1.3-6h3a8 8 0 0 1-4.3 6z"/></svg>www.keystoneridgebuilders.homes</li>
  </ul>
  <div class="trust">
    <p>Fully Licensed &amp; Insured</p>
    <svg class="stars" viewBox="0 0 176 32" role="img" aria-label="Five stars">
      <use href="#star" x="0" fill="url(#starGold)"/><use href="#star" x="36" fill="url(#starGold)"/>
      <use href="#star" x="72" fill="url(#starGold)"/><use href="#star" x="108" fill="url(#starGold)"/>
      <use href="#star" x="144" fill="url(#starGold)"/>
    </svg>
    <p>by Local Homeowners</p>
  </div>
  <div class="band band--cta">Schedule Your Free Design-Build Starter Session Today!</div>
</section>

<section class="card card--back">
  <div class="band band--top"></div>
  <div class="brand-mark" role="img" aria-label="Tallow Dwellings brand mark"></div>
  <h2 class="brand-name">TALLOW DWELLINGS</h2>
  <p class="brand-tagline">BUILT TO INSPIRE</p>
  <div class="band band--footer">Proudly serving Southwest Louisiana with Quality Craftsmanship &amp; Financing</div>
</section>
</body>
</html>
```